Home Page Design (PSD Only) - Ecommerce - Yarn, Apparel and Socks

We need a new home page design for our e-commerce site WoolHarborShop.com.
Our team will create the HTML/CSS using the Bootstrap framework. We just need the final PSD and slices. Our brand/logo will remain however our focus has shifted to two key product categories. 1: Yarn 2: Socks. We also sell products in the other categories but these will not be the focus and jewelry will likely go away.

Our socks and yarn are focused on "Affordable Luxury" We carry over 2000 yarns (Huge Selection) and have the largest selection on the internet for Alpaca Socks.

Our buyers are very different. Most yarn buyers are women 25-55 who are very tactile. They want to feel the yarn so this somehow needs to come through. Clean and Warm, Affordable Luxury.

Our sock buyers buy premium socks ($15-20/pair) are split male/female and have little interest in Yarn or Knitting. I realize we should likely have 2 different sites but we've spent 7 years building the brand and have loyalty from both markets and are not getting x-sell. Especially knitters who buy our socks and stuffed bears, etc for gifts.

We'll be moving toward a new responsive design based on the Bootstrap framework under the hood.
Updates

Target Market(s)

Women for the Yarn (knitters). Split 60F/40M for socks
Current site is blue. Feel free to update the colors to make the site more attractive for women.

Industry/Entity Type

E-Commerce

Requirements
Must have
• Rotating Hero, Global Search, Must incorporate our blue logo (or inverse). Social bar for Chirpwave, Friendloop, Pinboardly, Skeinly (yarn social site), Loopnotes (yarn social site).
Can use warm colors to appeal more to women.
Must support a responsive design (bootstrap)
Nice to have
• Site should resonate with Knitters but not alienate users who just come to shop for Socks, Stuffed Bears, Sweaters, etc.
Clean, simple design, but with warmth and upscale feeling.
Yarn sites: skeinmart.com, loopvalley.com
Sock/Apparel Sites: toastytoes.com, stridewellco.com, maplebrook.com, dunro.com

I've added some initial comps that tested OK but early feedback was it was too plain and lacked emotional appeal.

```html
<!DOCTYPE html>
<html lang="en">
<head>
<meta charset="utf-8">
<title>WoolHarborShop.com – Home</title>
<link rel="stylesheet" href="https://fonts.googleapis.com/css2?family=Ubuntu:wght@300;400;500&family=Source+Sans+3:wght@400;600&display=swap">
<style>
:root{
  --page:#c1985b;
  --nav-bg:#fcf3c6;
  --nav-border:#f3e29a;
  --ink:#3b2c1a;
  --blue:#1f74c0;
  --blue-overlay:rgba(28,112,196,.88);
  --blue-btn:#2a77b9;
  --bronze-btn:#a5763f;
  --white:#ffffff;
  --footer-bg:#f3ebe0;
  --footer-head:#5a4630;
  --footer-link:#c39b6b;
  --footer-muted:#b8ab9a;
  --support:#1d72c2;
}
*{box-sizing:border-box;margin:0;padding:0}
html,body{width:1107px;height:1200px;overflow:hidden}
body{background:var(--page);font-family:"Ubuntu",sans-serif;color:var(--ink);position:relative}
.abs{position:absolute}

/* header */
.utility{top:11px;right:60px;display:flex;gap:9px;font-size:11px;color:var(--white);align-items:center}
.utility span+span{border-left:1px solid rgba(255,255,255,.5);padding-left:9px}
.cart-icon{width:16px;height:14px}
.brand{top:38px;left:118px;font-size:34px;font-weight:400;color:var(--white);letter-spacing:1px}
.brand small{display:block;font-size:15px;text-align:right;letter-spacing:1px;margin-top:-4px}
.support{top:55px;left:835px;display:flex;gap:7px;align-items:center;color:var(--support)}
.support .label{font-size:12.5px;font-weight:300}
.support .phone{font-size:18px;font-weight:300;line-height:1}

/* nav */
.nav{top:111px;left:101px;width:905px;height:46px;background:var(--nav-bg);border:2px solid var(--nav-border);display:flex;align-items:center;padding-left:6px}
.nav a{font-size:13px;color:var(--ink);text-decoration:none;padding:0 14px;border-right:1px solid #e7d9a6;line-height:24px}
.nav a:nth-child(8){border-right:none}
.search{margin-left:auto;margin-right:4px;width:228px;height:32px;background:var(--white);border:1px solid #ece3c0;display:flex;align-items:center;justify-content:space-between;padding:0 10px;font-size:12px;color:#aaa}

/* hero */
.hero-main{top:166px;left:101px;width:646px;height:424px;background:linear-gradient(100deg,#c35a3b 0%,#6fa0b0 25%,#d0a442 45%,#b84e8e 65%,#c08f6b 85%,#b98c62 100%)}
.hero-caption{top:401px;left:120px;width:555px;height:166px;background:var(--blue-overlay);color:var(--white);padding:22px 20px}
.hero-caption h1{font-size:29px;font-weight:400;letter-spacing:-.3px}
.hero-caption p{font-size:11.5px;line-height:18px;margin-top:10px}
.btn{display:inline-block;font-size:11.5px;text-decoration:none;text-align:center;border-radius:2px}
.btn-light{background:var(--white);color:var(--ink);width:90px;height:24px;line-height:24px;margin-top:12px}
.promo-top{top:166px;left:748px;width:258px;height:268px;background:linear-gradient(180deg,#f2ede7,#e6dcd0)}
.promo-photo{position:absolute;right:0;top:0;width:140px;height:268px;background:linear-gradient(180deg,#ece4da,#d9cfc4 70%,#bfa688)}
.promo-text{position:absolute;left:13px;top:46px;width:100px}
.promo-text h2{font-size:17px;font-weight:400;line-height:16px;color:#5a4a3a}
.promo-text p{font-size:10.5px;line-height:15.5px;color:#a99a88;margin-top:8px;font-weight:300}
.promo-text a{display:block;margin-top:7px;font-size:13px;color:#5a4a3a;text-decoration:none}
.promo-bottom{top:435px;left:748px;width:258px;height:155px;background:radial-gradient(circle at 50% 40%,#8fa38a,#a7895e 60%,#d8cdb8)}
.promo-band{position:absolute;left:0;bottom:0;width:100%;height:34px;background:var(--blue-overlay);color:var(--white);font-size:14.5px;line-height:34px;padding-left:14px}

/* categories */
.category{top:614px;width:275px}
.category h3{font-size:14px;font-weight:400;text-align:center;color:#3f3223}
.category .photo{margin-top:10px;height:164px;box-shadow:0 2px 6px rgba(0,0,0,.25)}
.category p{margin-top:22px;font-size:11.5px;line-height:17px;color:var(--white);font-weight:300}
.btn-cat{margin-top:9px;width:90px;height:24px;line-height:24px;color:var(--white)}
.btn-blue{background:var(--blue-btn)}
.btn-bronze{background:var(--bronze-btn)}

/* footer */
.footer{top:941px;left:0;width:1107px;height:259px;background:var(--footer-bg);font-family:"Source Sans 3",sans-serif}
.f-head{font-size:11.5px;font-weight:600;color:var(--footer-head);letter-spacing:.3px}
.f-links{font-size:12px;line-height:15.6px;color:var(--footer-link)}
.newsletter-input{width:208px;height:25px;background:var(--white);border:1px solid #ddd2c2}
.disclaimer{font-size:9px;line-height:11px;color:var(--footer-muted);width:212px}
.social{display:flex;gap:8px}
.social span{width:26px;height:26px;border-radius:2px;background:var(--blue-btn)}
.copyright{font-size:12px;line-height:17px;color:#6b5a47}
.badges{top:196px;left:386px;display:flex;gap:0;align-items:center}
.badge{position:absolute;border-radius:2px}
</style>
</head>
<body>

<header>
  <div class="utility abs">
    <span>Welcome, ( log in )</span><span>Your Account</span><span>Cart (empty)</span>
    <svg class="cart-icon" viewBox="0 0 16 14" aria-hidden="true"><path d="M0 1h3l2 8h9l2-6H4.5" fill="none" stroke="#f5e8d2" stroke-width="1.6"/><circle cx="6" cy="12" r="1.4" fill="#f5e8d2"/><circle cx="13" cy="12" r="1.4" fill="#f5e8d2"/></svg>
  </div>
  <div class="brand abs">WoolHarbor<small>SHOP</small></div>
  <div class="support abs">
    <svg width="32" height="34" viewBox="0 0 32 34" aria-hidden="true"><path d="M4 18v-4a12 12 0 0 1 24 0v4" fill="none" stroke="currentColor" stroke-width="2.5"/><rect x="2" y="16" width="6" height="10" rx="2" fill="currentColor"/><rect x="24" y="16" width="6" height="10" rx="2" fill="currentColor"/><path d="M27 26q0 6-9 6" fill="none" stroke="currentColor" stroke-width="2"/></svg>
    <div><div class="label">24/7 Online Support</div><div class="phone">1-300-555-019</div></div>
  </div>
</header>

<nav class="nav abs">
  <a href="#">Home</a><a href="#">Yarn &amp; Fiber</a><a href="#">Socks</a><a href="#">Clothing</a><a href="#">Home Goods</a><a href="#">Jewelry</a><a href="#">Clearance</a><a href="#">Contact Us</a>
  <div class="search">Search
    <svg width="14" height="14" viewBox="0 0 14 14" aria-hidden="true"><circle cx="6" cy="6" r="4.5" fill="none" stroke="#999" stroke-width="1.6"/><path d="M9.5 9.5 13 13" stroke="#999" stroke-width="1.8"/></svg>
  </div>
</nav>

<section>
  <div class="hero-main abs" role="img" aria-label="Row of feet wearing colourful striped knitted socks beside balls of yarn"></div>
  <div class="hero-caption abs">
    <h1>Free Shipping in USA Over $75 Order.</h1>
    <p>Lorem Ipsum est simplement faux texte employé dans la sition misen page avant impression.<br>Le Lorem Ipsum est le faux texte standard.</p>
    <a class="btn btn-light" href="#">Read More</a>
  </div>
  <div class="promo-top abs">
    <div class="promo-photo" role="img" aria-label="Legs in argyle knee socks and white sneakers"></div>
    <div class="promo-text">
      <h2>Get Your’s Now</h2>
      <p>Lorem Ipsum est simplement du faux texte em-ployé dans la sition et la misen page</p>
      <a href="#">Learn More</a>
    </div>
  </div>
  <div class="promo-bottom abs" role="img" aria-label="Basket full of colourful yarn balls">
    <div class="promo-band">30% Off on Special Yarn Products</div>
  </div>
</section>

<section>
  <div class="category abs" style="left:101px">
    <h3>Women</h3>
    <div class="photo" role="img" aria-label="Woman in a white cardigan outdoors among greenery" style="background:linear-gradient(135deg,#3f5a2e,#6d7d4a 40%,#e7e1d8 70%,#4a5a35)"></div>
    <p>Lorem Ipsum est simplement du faux texte employé dans la sition et la misen page avant impression. Le Lorem Ipsum est le .</p>
    <a class="btn btn-cat btn-blue" href="#">Read More</a>
  </div>
  <div class="category abs" style="left:417px">
    <h3>Men</h3>
    <div class="photo" role="img" aria-label="Man in a cream knit cardigan against a bright background" style="background:linear-gradient(180deg,#f6f7f4,#e6e6df 55%,#d8d2c2)"></div>
    <p>Lorem Ipsum est simplement du faux texte employé dans la sition et la misen page avant impression. Le Lorem Ipsum est le .</p>
    <a class="btn btn-cat btn-bronze" href="#">Read More</a>
  </div>
  <div class="category abs" style="left:731px">
    <h3>Kids</h3>
    <div class="photo" role="img" aria-label="Child in pink hugging a fluffy stuffed toy" style="background:radial-gradient(circle at 55% 45%,#7b5a3e,#b08e72 35%,#e99ac0 65%,#f0a9cc)"></div>
    <p>Lorem Ipsum est simplement du faux texte employé dans la sition et la misen page avant impression. Le Lorem Ipsum est le .</p>
    <a class="btn btn-cat btn-bronze" href="#">Read More</a>
  </div>
</section>

<footer class="footer abs">
  <div class="abs" style="left:118px;top:42px">
    <div class="f-head">NEWSLETTER</div>
    <div class="newsletter-input" style="margin-top:12px;position:relative">
      <svg style="position:absolute;right:6px;top:6px" width="13" height="13" viewBox="0 0 13 13" aria-hidden="true"><circle cx="6.5" cy="6.5" r="5.6" fill="none" stroke="#555" stroke-width="1.1"/><path d="M5 4l3 2.5L5 9z" fill="#555"/></svg>
    </div>
    <p class="disclaimer" style="margin-top:6px">By entering my email address, I certify that the information, I am providing is accurate and that I am at least 18 years of age.</p>
  </div>
  <div class="abs" style="left:118px;top:150px;display:flex;align-items:center;gap:22px">
    <div class="f-head">FOLLOW US</div>
    <div class="social">
      <span role="img" aria-label="Friendloop"></span>
      <span role="img" aria-label="Chirpwave" style="background:#5aa9dc"></span>
      <span role="img" aria-label="Linkwise"></span>
    </div>
  </div>
  <div class="copyright abs" style="left:117px;top:201px">Copyright 2012 Website Name.<br>All Rights Reserved.</div>

  <div class="abs" style="left:391px;top:42px">
    <div class="f-head">WHISHLIST</div>
    <div class="f-links" style="margin-top:9px">It’s easy to tag &nbsp;your favorites.<br>get started...</div>
    <div class="f-head" style="margin-top:34px">ORDER BY PHONE</div>
    <div class="f-links" style="margin-top:9px;font-size:13px">1-000-000-000</div>
  </div>
  <div class="abs" style="left:569px;top:42px">
    <div class="f-head">WHY BUY FROM US</div>
    <div class="f-links" style="margin-top:9px">Shipping &amp; Return<br>Seure Shopping<br>International<br>Shipping<br>Affiliates<br>Group Sales</div>
  </div>
  <div class="abs" style="left:743px;top:42px">
    <div class="f-head">ABOUT US</div>
    <div class="f-links" style="margin-top:9px">Customer Service<br>Privacy Policy<br>Site Map<br>Press Room</div>
  </div>
  <div class="abs" style="left:885px;top:42px">
    <div class="f-head">MY ACCOUNT</div>
    <div class="f-links" style="margin-top:9px">Sign in<br>View Cart<br>Wish List<br>Track My order<br>Help</div>
  </div>

  <div class="badge" role="img" aria-label="Gift card badge" style="left:386px;top:197px;width:62px;height:40px;background:linear-gradient(135deg,#e3cc87,#c9a95c)"></div>
  <div class="badge" role="img" aria-label="Accreditation badge" style="left:489px;top:195px;width:26px;height:42px;background:#1f5f96"></div>
  <div class="badge" role="img" aria-label="Social page badge" style="left:542px;top:202px;width:89px;height:28px;background:#e9edf4;border:1px solid #b9c3d6"></div>
  <div class="badge" role="img" aria-label="Checkout badge" style="left:652px;top:197px;width:37px;height:40px;background:#fff;border:1px solid #ccc"></div>
  <div class="badge" role="img" aria-label="Accepted payment methods" style="left:719px;top:196px;width:70px;height:40px;background:#fff;border:1px solid #ddd"></div>
  <div class="badge" role="img" aria-label="Payment processor seal" style="left:818px;top:196px;width:42px;height:42px;border-radius:50%;background:#e7cf6a"></div>
  <div class="badge" role="img" aria-label="Security verification seal" style="left:878px;top:205px;width:92px;height:24px;background:#fff;border:1px solid #bbb"></div>
</footer>

</body>
</html>
```